Software engineering company needs business card

I need a cool business card. Company: Soft Belan Brindlewood Ave 41 58207 Sincity Name: Gerald Vanholt CEO / Managing Director & Owner

```html
<!DOCTYPE html>
<html lang="en">
<head>
<meta charset="utf-8">
<title>Soft Belan – Business Card</title>
<link rel="stylesheet" href="https://fonts.googleapis.com/css2?family=Didact+Gothic&family=Oswald:wght@300&family=Questrial&display=swap">
<style>
  :root {
    --green: #8dcf2a;
    --grey: #58585b;
    --card: #000000;
    --paper: #ffffff;
    --ink: #ffffff;
  }
  * { margin: 0; padding: 0; box-sizing: border-box; }
  html, body { width: 903px; height: 1200px; overflow: hidden; background: var(--paper); }
  .sheet { position: relative; width: 903px; height: 1200px; }
  .side-label {
    position: absolute; left: 0; width: 903px; text-align: center;
    font-family: "Oswald", sans-serif; font-weight: 300;
    color: var(--green); font-size: 44px; line-height: 1; letter-spacing: 1px;
  }
  .side-label.front { top: -4px; }
  .side-label.back { top: 634px; }
  .card {
    position: absolute; left: 2px; width: 900px;
    background: var(--card); border-radius: 34px; overflow: hidden;
  }
  .card.front { top: 58px; height: 517px; }
  .card.back { top: 684px; height: 515px; }

  .wordmark {
    position: absolute; display: flex; align-items: center; gap: 14px;
    font-family: "Questrial", sans-serif; color: var(--green);
    text-transform: uppercase; white-space: nowrap; line-height: 1;
  }
  .wordmark .dot { background: var(--green); display: block; }
  .front .wordmark { left: 24px; top: 120px; font-size: 66px; letter-spacing: 6px; }
  .front .wordmark .dot { width: 40px; height: 40px; }
  .back .wordmark { left: 0; width: 900px; justify-content: center; top: 128px; font-size: 96px; letter-spacing: 9px; gap: 22px; }
  .back .wordmark .dot { width: 56px; height: 56px; }

  .person { position: absolute; left: 51px; top: 308px; font-family: "Didact Gothic", sans-serif; }
  .person .name { color: var(--green); font-size: 41px; line-height: 1.1; letter-spacing: 1px; }
  .person .role { color: var(--ink); font-size: 21px; margin-top: 18px; }

  .contact { position: absolute; left: 487px; top: 273px; list-style: none; font-family: "Didact Gothic", sans-serif; color: var(--ink); font-size: 23px; }
  .contact li { position: absolute; left: 0; display: flex; align-items: flex-start; white-space: nowrap; }
  .contact svg { width: 30px; height: 30px; flex: none; margin-right: 16px; }
  .contact .phone { top: 0; }
  .contact .mail { top: 35px; }
  .contact .web { top: 76px; }
  .contact .addr { top: 117px; line-height: 1.4; }

  .back .url {
    position: absolute; left: 0; width: 900px; bottom: 14px; text-align: center;
    font-family: "Didact Gothic", sans-serif; font-weight: 700; color: var(--ink);
    font-size: 36px; letter-spacing: 1px; -webkit-text-stroke: 0.8px var(--ink);
  }
</style>
</head>
<body>
<main class="sheet">
  <h2 class="side-label front">FRONT SIDE</h2>
  <section class="card front">
    <div class="wordmark"><span class="dot"></span>Soft Belan</div>

    <div class="person">
      <p class="name">Gerald Vanholt</p>
      <p class="role">CEO / Geschäftsführer &amp; Inhaber</p>
    </div>

    <ul class="contact">
      <li class="phone">
        <svg viewBox="0 0 24 24"><path fill="var(--green)" d="M6.6 2.5l3 3.2-1.9 2.4c1.2 2.6 3.2 4.7 6 6.1l2.4-1.9 3.3 3-2 3.2C10 18 5.6 13.6 3.4 5z"/></svg>
        <span>+49-123456789</span>
      </li>
      <li class="mail">
        <svg viewBox="0 0 24 24"><path fill="var(--green)" d="M2 5h20v14H2z"/><path d="M2.5 5.5l9.5 8 9.5-8M2.5 18.5l7-6.5m12 6.5l-7-6.5" stroke="var(--card)" stroke-width="1.6" fill="none"/></svg>
        <span>name@domain.com</span>
      </li>
      <li class="web">
        <svg viewBox="0 0 24 24" fill="none" stroke="var(--green)" stroke-width="1.6"><circle cx="12" cy="12" r="10"/><ellipse cx="12" cy="12" rx="4.5" ry="10"/><path d="M2 12h20M4 6.5h16M4 17.5h16"/></svg>
        <span>www.name.com</span>
      </li>
      <li class="addr">
        <svg viewBox="0 0 24 24" fill="none" stroke="var(--green)" stroke-width="1.8"><path d="M12 22s-7-7.5-7-12.5a7 7 0 0 1 14 0C19 14.5 12 22 12 22z"/><circle cx="12" cy="9.5" r="2.6"/></svg>
        <span>Brindlewood Ave 41, 58207,<br>Sincity.</span>
      </li>
    </ul>
  </section>

  <h2 class="side-label back">BACK SIDE</h2>
  <section class="card back">
    <div class="wordmark"><span class="dot"></span>Soft Belan</div>
    <p class="url">www.name.com</p>
  </section>
</main>
</body>
</html>
```